Wine Label for Commemorative Wine Bottle

We are producing a special Estate blend of wine, and want to have a unique "family" label. We have an idea of what we want, and would like for someone to make it look good by adding some creative flair to it. I am attaching the basic idea of the label we have, as well as a pic of a bottle that captures the basic style we are going for. We are ok with playing with the color palette, and would like some "gold" in our design.

Font styles to use
Decorative

```html
<!DOCTYPE html>
<html lang="en">
<head>
<meta charset="utf-8">
<title>27 Vela – Estate Label</title>
<link href="https://fonts.googleapis.com/css2?family=Cinzel:wght@400;600;700&display=swap" rel="stylesheet">
<style>
  :root {
    --backdrop: #e8e0d2;
    --label-paper: #fbfbf8;
    --gold: #bdb43d;
    --gold-light: #cdc566;
    --gold-dark: #8f8828;
    --ink: #3d3c33;
    --ribbon-ink: #4a4620;
  }
  html, body {
    margin: 0;
    padding: 0;
    width: 1200px;
    height: 857px;
    overflow: hidden;
    background: var(--backdrop);
  }
  .canvas {
    position: relative;
    width: 1200px;
    height: 857px;
    display: flex;
    align-items: center;
    justify-content: center;
  }
  .wine-label {
    width: 420px;
    height: 630px;
    filter: drop-shadow(0 6px 14px rgba(60, 48, 30, 0.18));
  }
  .label-shape { fill: var(--label-paper); }
  .label-rule { fill: none; stroke: var(--gold); stroke-width: 2; }
  .star { fill: var(--label-paper); stroke: var(--gold-light); stroke-width: 1.2; }
  .dedication {
    font-family: 'Cinzel', serif;
    font-size: 13px;
    font-weight: 600;
    fill: var(--ink);
    letter-spacing: 0.6px;
  }
  .ribbon-body { fill: var(--gold-light); }
  .ribbon-tail { fill: var(--gold); }
  .ribbon-fold { fill: var(--gold-dark); }
  .ribbon-text {
    font-family: 'Cinzel', serif;
    font-size: 19px;
    font-weight: 600;
    letter-spacing: 3px;
    fill: var(--ribbon-ink);
  }
  .vintage-number {
    font-family: 'Cinzel', serif;
    font-size: 140px;
    font-weight: 700;
    fill: var(--gold);
  }
  .wine-name {
    font-family: 'Cinzel', serif;
    font-size: 22px;
    letter-spacing: 14px;
    fill: var(--ink);
  }
  .estate-line {
    font-family: 'Cinzel', serif;
    font-size: 14px;
    font-weight: 600;
    letter-spacing: 0.8px;
    fill: var(--ink);
  }
  .bottle-number-box { fill: var(--gold); }
  .bottle-number {
    font-family: 'Cinzel', serif;
    font-size: 15px;
    font-weight: 600;
    fill: var(--label-paper);
  }
</style>
</head>
<body>
<main class="canvas">
  <svg class="wine-label" viewBox="0 0 420 630" xmlns="http://www.w3.org/2000/svg">
    <polygon class="label-shape" points="210,0 420,60 420,525 210,630 0,525 0,60"/>
    <polygon class="label-rule" points="210,10 410,67 410,519 210,619 10,519 10,67"/>

    <g class="stars">
      <polygon class="star" transform="translate(184,70)" points="0,-9 2.6,-3 9,-2.8 4,1.6 5.6,8 0,4.5 -5.6,8 -4,1.6 -9,-2.8 -2.6,-3"/>
      <polygon class="star" transform="translate(210,66) scale(1.3)" points="0,-9 2.6,-3 9,-2.8 4,1.6 5.6,8 0,4.5 -5.6,8 -4,1.6 -9,-2.8 -2.6,-3"/>
      <polygon class="star" transform="translate(236,70)" points="0,-9 2.6,-3 9,-2.8 4,1.6 5.6,8 0,4.5 -5.6,8 -4,1.6 -9,-2.8 -2.6,-3"/>
    </g>

    <text class="dedication" x="210" y="118" text-anchor="middle">Dedicated to Owen and Clara</text>
    <text class="dedication" x="210" y="136" text-anchor="middle">The future of Cedar Ridge Vineyard</text>

    <g class="ribbon">
      <path class="ribbon-tail" d="M14,232 L58,226 L58,270 L14,276 L30,254 Z"/>
      <path class="ribbon-tail" d="M406,232 L362,226 L362,270 L406,276 L390,254 Z"/>
      <path class="ribbon-fold" d="M44,214 L58,226 L58,250 Z"/>
      <path class="ribbon-fold" d="M376,214 L362,226 L362,250 Z"/>
      <path class="ribbon-body" d="M44,214 Q210,184 376,214 L376,250 Q210,220 44,250 Z"/>
      <text class="ribbon-text" x="211" y="225" text-anchor="middle">THE ORIGINAL</text>
    </g>

    <text class="vintage-number" x="210" y="395" text-anchor="middle">27</text>
    <text class="wine-name" x="217" y="434" text-anchor="middle">VELA</text>

    <text class="estate-line" x="210" y="470" text-anchor="middle">Estate Harlow</text>
    <text class="estate-line" x="210" y="492" text-anchor="middle">2014</text>

    <rect class="bottle-number-box" x="163" y="540" width="94" height="36"/>
    <text class="bottle-number" x="210" y="563" text-anchor="middle">060</text>
  </svg>
</main>
</body>
</html>
```